Business Card for Web Design consulting firm

Business card designs for Web Design consulting firm

Target Market(s)

English speaking adults ages 30 - 60. Predominantly professional services eg. Doctor, Dentist

Industry/Entity Type

Consulting

Requirements
Must have
• Double sided card

```html
<!DOCTYPE html>
<html lang="en">
<head>
<meta charset="utf-8">
<title>Lumora – Business Card</title>
<link rel="stylesheet" href="https://fonts.googleapis.com/css2?family=Baskervville&display=swap">
<style>
  :root {
    --card-bg: #f2f2f2;
    --gap-bg: #ffffff;
    --ink: #4d4d4d;
    --accent: #f7981f;
    --ghost: #ebebeb;
  }
  * { margin: 0; padding: 0; box-sizing: border-box; }
  html, body {
    width: 887px;
    height: 1200px;
    overflow: hidden;
    background: var(--gap-bg);
  }
  body {
    position: relative;
    font-family: "Baskervville", "Baskerville", Georgia, serif;
    color: var(--ink);
  }
  .card {
    position: absolute;
    left: 0;
    width: 887px;
    background: var(--card-bg);
    overflow: hidden;
  }
  .card--front { top: 0; height: 574px; }
  .card--back { top: 625px; height: 575px; }

  .brand-name {
    position: absolute;
    font-weight: 400;
    color: var(--ink);
    line-height: 1;
    white-space: nowrap;
  }
  .card--front .brand-name {
    left: 37px;
    top: 128px;
    font-size: 50px;
    letter-spacing: 0.2em;
  }
  .brand-ghost {
    position: absolute;
    left: 28px;
    top: 355px;
    font-size: 120px;
    color: var(--ghost);
    letter-spacing: 0.3em;
    line-height: 1;
    white-space: nowrap;
  }

  .person-name {
    position: absolute;
    left: 524px;
    top: 134px;
    font-size: 44px;
    font-weight: 400;
    line-height: 1;
    white-space: nowrap;
  }
  .person-role {
    position: absolute;
    left: 606px;
    top: 188px;
    font-size: 31px;
    color: var(--accent);
    line-height: 1;
    white-space: nowrap;
  }
  .contact {
    position: absolute;
    left: 605px;
    top: 372px;
    list-style: none;
    font-size: 28px;
    line-height: 35px;
    white-space: nowrap;
  }

  .card--back .brand-name {
    left: 0;
    width: 887px;
    top: 340px;
    text-align: center;
    font-size: 90px;
    letter-spacing: 0.25em;
    text-indent: 0.25em;
  }
</style>
</head>
<body>
  <section class="card card--front">
    <div class="brand-ghost" aria-hidden="true">LUMORA</div>
    <div class="brand-name">LUMORA</div>
    <h1 class="person-name">Daniel Harper</h1>
    <p class="person-role">Sales Manager</p>
    <ul class="contact">
      <li>P: 07 55501234</li>
      <li>M: 0455501234</li>
      <li>@: info@lumora.com</li>
      <li>www.lumora.com</li>
    </ul>
  </section>

  <section class="card card--back">
    <div class="brand-name">LUMORA</div>
  </section>
</body>
</html>
```